Gourmet Chocolate Chip cookie company e-commerce website design

We would like to create a landing page for an e-commerce site for a gourmet chocolate chip cookie business. We are in the process of finalizing the "About Us" story.... A chic, clean, fresh, (don't forget yummy) site for "Lulu's Bakes". Offers a "Cookies like Mom makes" for anyone who is missing home. Our cookies are homemade, artisan, small batch product. This will be a direct to consumer site for care packages, gifts, occasions as well as business and corporate events. For the landing page, we would like customers to be able to place an order and or inquire further about our product as well as links to social media (Instagram, Facebook and Linkedin and email). We would like to transition by end of year to a full Shopify platform, for customers and consumers to process and ship all orders. We do not have official photography yet, but we have included some sneak peaks from inside the kitchen. A couple of key phrases that describe our brand: "If you love cookie dough, you will love these cookies" "It tastes as good as it looks" "Its pure love and happiness" "Puts a smile on your face" "Tastes like home" These cookies have been in the family for 40+ years and its time to share! Our goal is to make this a lifestyle brand.
https://www.dailyvexmo.example/2018/08/30/health/baked-treats-craving-study-pelton/index.html
a tester shopify page:
https://kqzt7h2vrend5xa8-5817204926.storedemo.example/
Target Market(s)
direct to consumer focusing on 'the gift giver', being that this is a gourmet product, the sell price falls under the 'luxury category'. Goal is to target occasions, college kids, corporate and business events
Number of Pages Required
4 page
Font styles to use
Other font styles liked:
- see branding and logos attached
Requirements
Must have
- Initially, a landing page is a necessity and then a full workable website on the Shopify platform.
- Full website will include, shop, about us, gallery (linked to instagram), press, cart, terms and conditions. (access to all social media accounts)
Nice to have
- Inspo brands we love:
- Meadowlass Blooms
- Hollis Vantree
- Pemberly Quaid
- Crumbtops
Should not have
- SHOULD NOT LOOK LIKE AUNT WILLOWBY
- Please call or email with questions

```html
<!DOCTYPE html>
<html lang="en">
<head>
<meta charset="utf-8">
<title>Lulu's Bakes</title>
<link rel="stylesheet" href="https://fonts.googleapis.com/css2?family=Poppins:wght@400;500;600;700&display=swap">
<style>
  :root{
    --ink:#1f1f1f;
    --topbar:#222222;
    --muted:#8a8a8a;
    --line:#bdbdbd;
    --accent:#e32c2c;
    --white:#ffffff;
    --footer:#050505;
    --dough:#b99466;
    --dough-dark:#7d5c3a;
    --marble:#d9d6d2;
  }
  *{box-sizing:border-box;margin:0;padding:0}
  html,body{width:710px;height:1200px;overflow:hidden;background:var(--white)}
  body{position:relative;font-family:'Poppins',sans-serif;color:var(--ink)}
  .abs{position:absolute}

  .topbar{left:0;top:0;width:710px;height:18px;background:var(--topbar);color:#e6e6e6;font-size:5.5px;display:flex;align-items:center;justify-content:space-between;padding:0 148px}
  .topbar-social{display:flex;gap:6px}
  .topbar-social span{width:6px;height:6px;border-radius:50%;background:#9a9a9a}

  .header{left:0;top:18px;width:710px;height:56px}
  .main-nav{left:147px;top:23px;display:flex;gap:13px;font-size:5.5px}
  .brand{left:306px;top:6px;width:96px;height:38px;border:2px solid var(--ink);display:flex;align-items:center;justify-content:center;font-size:11px;font-weight:600;box-shadow:3px 3px 3px rgba(0,0,0,.18);background:var(--white)}
  .search-icon{left:491px;top:21px}
  .contact-btn{left:506px;top:17px;width:43px;height:16px;border:1px solid var(--line);font-size:5.2px;display:flex;align-items:center;justify-content:center}
  .bag-icon{left:555px;top:19px}

  .hero{left:0;top:74px;width:710px;height:218px;background:linear-gradient(180deg,#5d5d5a 0%,#4a4845 55%,#3f3b37 100%);display:flex;flex-direction:column;align-items:center}
  .hero-frame{left:3px;top:3px;right:3px;bottom:3px;border:1px solid rgba(255,255,255,.7)}
  .hero h1{margin-top:75px;color:var(--white);font-size:20px;font-weight:700;letter-spacing:.2px}
  .hero p{margin-top:6px;color:#f0f0f0;font-size:7px}
  .shop-now{margin-top:13px;width:66px;height:20px;background:var(--accent);color:var(--white);font-size:5.2px;font-weight:600;display:flex;align-items:center;justify-content:center}

  .section-title{left:0;width:710px;text-align:center;font-size:12.5px;font-weight:600}
  .product-row{left:147px;width:416px;display:flex;gap:8px}
  .product{width:98px}
  .product-photo{width:98px;height:139px}
  .product-meta{display:flex;justify-content:space-between;margin-top:10px;font-size:5.3px}
  .product-price{color:var(--accent);font-weight:600;font-size:6.5px}
  .add-cart{margin-top:5px;width:52px;height:15px;border:1px solid var(--line);font-size:4.6px;display:flex;align-items:center;justify-content:center;color:#555}

  .tile{display:flex;align-items:flex-end;padding:0 0 12px 9px}
  .tile span{color:var(--white);font-size:5.5px;font-weight:600;border-bottom:1px solid rgba(255,255,255,.8);padding-bottom:2px}

  .photo-dough{background:linear-gradient(160deg,#cfc7bd 0%,var(--dough) 55%,var(--dough-dark) 100%)}
  .photo-tray{background:linear-gradient(170deg,#c8c4bf 0%,#d7b58a 60%,#b78d5e 100%)}
  .photo-kettle{background:linear-gradient(180deg,#9a9894 0%,#5c5a58 40%,#c9a277 100%)}
  .photo-bowl{background:radial-gradient(circle at 50% 45%,#b88c5a 0%,#c9a87f 45%,var(--marble) 75%)}
  .photo-check{background:linear-gradient(135deg,#2b2b2b 0%,#8b8b8b 50%,#e9e9e9 100%)}
  .photo-flowers{background:linear-gradient(180deg,#6f7868 0%,#4a4d46 60%,#2d2d2d 100%)}
  .photo-kitchen{background:linear-gradient(180deg,#a5a4a0 0%,#6f5c48 60%,#5a4530 100%)}

  .features{left:147px;top:1008px;width:416px;display:flex;justify-content:space-between}
  .feature{width:92px;text-align:center}
  .feature svg{display:block;margin:0 auto 5px}
  .feature h3{font-size:6px;font-weight:500;margin-bottom:4px}
  .feature p{font-size:4.2px;color:var(--muted);line-height:1.6}

  .footer{left:0;top:1096px;width:710px;height:104px;background:var(--footer);color:var(--white)}
  .footer-brand{left:147px;top:19px;width:96px;height:37px;border:2px solid var(--white);display:flex;align-items:center;justify-content:center;font-size:11px;font-weight:600}
  .footer-nav{left:303px;top:32px;display:flex;gap:13px;font-size:5.3px}
  .footer-social{left:453px;top:24px;display:flex;gap:5px}
  .footer-social span{width:18px;height:18px;border-radius:50%;background:var(--white)}
  .copyright{left:0;top:81px;width:710px;text-align:center;font-size:5.5px}
  .copyright b{font-weight:600}
</style>
</head>
<body>

<div class="abs topbar">
  <span>Phone Number : 123 456 6789</span>
  <div class="topbar-social"><span></span><span></span><span></span><span></span><span></span></div>
</div>

<header class="abs header">
  <nav class="abs main-nav"><span>Home</span><span>About</span><span>Gallery</span><span>Shop</span></nav>
  <div class="abs brand">Lulu's Bakes</div>
  <svg class="abs search-icon" width="9" height="9" viewBox="0 0 10 10"><circle cx="4" cy="4" r="3" fill="none" stroke="#1f1f1f" stroke-width="1.2"/><line x1="6.2" y1="6.2" x2="9" y2="9" stroke="#1f1f1f" stroke-width="1.2"/></svg>
  <div class="abs contact-btn">Contac us</div>
  <svg class="abs bag-icon" width="8" height="9" viewBox="0 0 8 9"><rect x="0.6" y="2.5" width="6.8" height="6" fill="none" stroke="#1f1f1f" stroke-width="0.9"/><path d="M2.3 2.5V1.8a1.7 1.7 0 0 1 3.4 0v.7" fill="none" stroke="#1f1f1f" stroke-width="0.9"/></svg>
</header>

<section class="abs hero" role="img" aria-label="Kitchen counter with white roses and gift boxes tied with striped ribbon">
  <div class="abs hero-frame"></div>
  <h1>ITS PURE LOVE AND HAPPINESS</h1>
  <p>Lorem Ipsum is simply dummy text of the printing and typesetting industry</p>
  <div class="shop-now">SHOP NOW</div>
</section>

<h2 class="abs section-title" style="top:309px">Shop by category</h2>
<div class="abs product-row" style="top:347px">
  <div class="product"><div class="product-photo photo-tray" role="img" aria-label="Rows of chocolate chip cookies"></div><div class="product-meta"><span>Lulu's Bakes</span><span class="product-price">$150.00</span></div><div class="add-cart">ADD TO CART</div></div>
  <div class="product"><div class="product-photo photo-dough" role="img" aria-label="Bowl of cookie dough on a counter"></div><div class="product-meta"><span>Chocolate Chip</span><span class="product-price">$150.00</span></div><div class="add-cart">ADD TO CART</div></div>
  <div class="product"><div class="product-photo photo-kettle" role="img" aria-label="Checkered kettle above a tray of cookies"></div><div class="product-meta"><span>Tastes like home</span><span class="product-price">$150.00</span></div><div class="add-cart">ADD TO CART</div></div>
  <div class="product"><div class="product-photo photo-bowl" role="img" aria-label="Glass bowl of cookie dough from above"></div><div class="product-meta"><span>Lulu's Bakes</span><span class="product-price">$150.00</span></div><div class="add-cart">ADD TO CART</div></div>
</div>

<div class="abs tile photo-kettle" style="left:147px;top:558px;width:151px;height:183px" role="img" aria-label="Checkered kettle and clock over a tray of cookies"><span>CHOCOLATE CHIP</span></div>
<div class="abs tile photo-check" style="left:302px;top:558px;width:106px;height:88px" role="img" aria-label="Black and white checkered platter"><span>CHOCOLATE CHIP</span></div>
<div class="abs tile photo-flowers" style="left:302px;top:652px;width:106px;height:89px" role="img" aria-label="Flowers and ribboned gift boxes"><span>LULU'S BAKES</span></div>
<div class="abs tile photo-kitchen" style="left:413px;top:558px;width:150px;height:183px" role="img" aria-label="Bowls of cookie dough in a kitchen"><span>TASTES LIKE HOME</span></div>

<h2 class="abs section-title" style="top:758px">Featured Product</h2>
<div class="abs product-row" style="top:796px">
  <div class="product"><div class="product-photo photo-kitchen" role="img" aria-label="Bowl of cookie dough in a kitchen"></div><div class="product-meta"><span>Chocolate Chip</span><span class="product-price">$150.00</span></div><div class="add-cart">ADD TO CART</div></div>
  <div class="product"><div class="product-photo photo-check" role="img" aria-label="Black and white checkered platter"></div><div class="product-meta"><span>Lulu's Bakes</span><span class="product-price">$150.00</span></div><div class="add-cart">ADD TO CART</div></div>
  <div class="product"><div class="product-photo photo-kettle" role="img" aria-label="Checkered kettle above a tray of cookies"></div><div class="product-meta"><span>Tastes like home</span><span class="product-price">$150.00</span></div><div class="add-cart">ADD TO CART</div></div>
  <div class="product"><div class="product-photo photo-tray" role="img" aria-label="Rows of chocolate chip cookies"></div><div class="product-meta"><span>Chocolate Chip</span><span class="product-price">$150.00</span></div><div class="add-cart">ADD TO CART</div></div>
</div>

<div class="abs features">
  <div class="feature">
    <svg width="32" height="22" viewBox="0 0 32 22" fill="none" stroke="#e32c2c" stroke-width="1.2"><rect x="1" y="3" width="19" height="13"/><path d="M20 7h6l4 5v4H20z"/><circle cx="7" cy="18" r="2.5" fill="#fff"/><circle cx="25" cy="18" r="2.5" fill="#fff"/></svg>
    <h3>FREE SHIPPING</h3><p>Lorem Ipsum is simply dummy text of<br>the printing and typesetting</p>
  </div>
  <div class="feature">
    <svg width="24" height="24" viewBox="0 0 24 24" fill="none" stroke="#e32c2c" stroke-width="1.4"><path d="M20 9a9 9 0 0 0-16-2"/><path d="M4 15a9 9 0 0 0 16 2"/><path d="M3 3v5h5"/><path d="M21 21v-5h-5"/></svg>
    <h3>GUARANTEE</h3><p>Lorem Ipsum is simply dummy text of<br>the printing and typesetting</p>
  </div>
  <div class="feature">
    <svg width="24" height="24" viewBox="0 0 24 24" fill="none" stroke="#e32c2c" stroke-width="1.2"><rect x="2" y="6" width="20" height="16"/><path d="M4 6l12-4 2 4"/><rect x="15" y="11" width="7" height="6"/><circle cx="18" cy="14" r="1"/></svg>
    <h3>CASH ON DELIVERY</h3><p>Lorem Ipsum is simply dummy text of<br>the printing and typesetting</p>
  </div>
  <div class="feature">
    <svg width="24" height="24" viewBox="0 0 24 24" fill="none" stroke="#e32c2c" stroke-width="1.2"><path d="M5 11a7 7 0 0 1 14 0"/><rect x="3" y="10" width="3" height="5"/><rect x="18" y="10" width="3" height="5"/><path d="M19 15c0 2-2 3-5 3"/><path d="M3 23c1-4 5-5 9-5s8 1 9 5"/></svg>
    <h3>SUPPORT</h3><p>Lorem Ipsum is simply dummy text of<br>the printing and typesetting</p>
  </div>
</div>

<footer class="abs footer">
  <div class="abs footer-brand">Lulu's Bakes</div>
  <nav class="abs footer-nav"><span>Home</span><span>About</span><span>Gallery</span><span>Shop</span></nav>
  <div class="abs footer-social"><span></span><span></span><span></span><span></span><span></span></div>
  <p class="abs copyright">Copyright © 2018 <b>Lulu's Bakes</b> .All Rights Reserved.</p>
</footer>

</body>
</html>
```